Business card for a shipping supplies business

Needing a business card design. Please see the logo. The logo with the white font should be used if there is a dark background.

We are looking for the following info on the card. Please see the sample info. We will need the info to be changed with a few different employee names and info but all will use the same template.

Business Name: The Crate Heron
Employee Name : Derek Malloy
Position: Account Manager
Address: 4827 W. Ridge 918 S.
Harlow Springs, KS 72348
email: Derek@thecrateheron.com
telephone: 866-417-2902 x 217
website: www.getcartonry.com

Target Market(s)

Businesses who ship products for online sales

Industry/Entity Type

Cardboard

Contact Information for Business Card

Name, title, address, website, logo, telephone number

Font styles to use
Sans Serif

Colors
EE7325
F08F49
F5BC92
FAE3D3
FDF4ED

Requirements
Must have
• Logo on back of card. Clean look, just logo, website address

```html
<!DOCTYPE html>
<html lang="en">
<head>
<meta charset="utf-8">
<title>The Crate Heron – Business Card</title>
<link rel="stylesheet" href="https://fonts.googleapis.com/css2?family=Montserrat:wght@500;600;700&family=Arimo:wght@400&display=swap">
<style>
  :root {
    --ink: #000000;
    --paper: #ffffff;
    --orange: #d2561c;
    --orange-bright: #ee7325;
    --backdrop: #ece8e4;
    --text: #111111;
  }
  * { box-sizing: border-box; margin: 0; padding: 0; }
  html, body { width: 1200px; height: 900px; overflow: hidden; }
  body {
    background: var(--backdrop);
    font-family: "Arimo", Arial, sans-serif;
    position: relative;
  }
  .card {
    position: absolute;
    left: 250px;
    width: 700px;
    height: 400px;
    overflow: hidden;
    box-shadow: 0 6px 18px rgba(0,0,0,.25);
  }
  .card--back { top: 35px; background: var(--ink); }
  .card--front { top: 465px; background: var(--paper); }

  /* back */
  .brand {
    position: absolute;
    left: 0; right: 0; top: 150px;
    display: flex; align-items: center; justify-content: center; gap: 16px;
  }
  .brand__dot {
    width: 38px; height: 38px; border-radius: 50%;
    background: var(--orange-bright);
  }
  .brand__name {
    font-family: "Montserrat", sans-serif;
    font-weight: 700;
    font-size: 46px;
    letter-spacing: 1px;
    color: var(--paper);
  }
  .card--back .website {
    position: absolute; left: 0; right: 0; top: 270px;
    text-align: center; font-size: 20px;
  }
  .website { color: var(--paper); }
  .website__domain { color: var(--orange-bright); }

  /* front */
  .front-wave { position: absolute; inset: 0; }
  .front-brand {
    position: absolute; right: 48px; top: 48px;
    display: flex; align-items: center; gap: 10px;
  }
  .front-brand__dot {
    width: 26px; height: 26px; border-radius: 50%;
    background: var(--orange-bright);
  }
  .front-brand__name {
    font-family: "Montserrat", sans-serif;
    font-weight: 700; font-size: 26px; color: var(--ink);
  }
  .person { position: absolute; left: 60px; top: 70px; }
  .person__name {
    font-family: "Montserrat", sans-serif;
    font-weight: 700; font-size: 30px; color: var(--ink);
    letter-spacing: .5px;
  }
  .person__surname { color: var(--orange); }
  .person__title {
    font-family: "Montserrat", sans-serif;
    font-weight: 500; font-size: 19px; color: var(--text); margin-top: 2px;
  }
  .contact {
    position: absolute; left: 72px; top: 165px;
    font-size: 19px; color: var(--text); line-height: 1.35;
  }
  .contact__line { display: flex; align-items: center; gap: 9px; }
  .contact__icon { width: 18px; height: 18px; flex: none; }
  .address { margin-top: 14px; font-size: 20px; line-height: 1.3; }
  .card--front .website {
    position: absolute; right: 40px; bottom: 50px; font-size: 19px;
  }
</style>
</head>
<body>
  <section class="card card--back" aria-label="Card back">
    <div class="brand">
      <span class="brand__dot"></span>
      <span class="brand__name">The Crate Heron</span>
    </div>
    <p class="website">www.<span class="website__domain">getcartonry</span>.com</p>
  </section>

  <section class="card card--front" aria-label="Card front">
    <svg class="front-wave" viewBox="0 0 700 400" preserveAspectRatio="none" aria-hidden="true">
      <path d="M0,350 C260,356 470,275 700,145 L700,400 L0,400 Z" fill="var(--ink)"/>
      <path d="M0,326 C240,328 420,278 560,210 C430,298 250,343 0,341 Z" fill="var(--orange)"/>
    </svg>

    <div class="front-brand">
      <span class="front-brand__dot"></span>
      <span class="front-brand__name">The Crate Heron</span>
    </div>

    <div class="person">
      <h1 class="person__name">DEREK <span class="person__surname">MALLOY</span></h1>
      <p class="person__title">Account Manager</p>
    </div>

    <div class="contact">
      <p class="contact__line">
        <svg class="contact__icon" viewBox="0 0 24 24" aria-hidden="true"><path fill="var(--orange)" d="M6.6 10.8a15.1 15.1 0 0 0 6.6 6.6l2.2-2.2a1 1 0 0 1 1-.25 11.4 11.4 0 0 0 3.6.57 1 1 0 0 1 1 1V20a1 1 0 0 1-1 1A17 17 0 0 1 3 4a1 1 0 0 1 1-1h3.5a1 1 0 0 1 1 1c0 1.25.2 2.45.57 3.57a1 1 0 0 1-.25 1z"/></svg>
        866-417-2902 x 217
      </p>
      <p class="contact__line">
        <svg class="contact__icon" viewBox="0 0 24 24" aria-hidden="true"><path fill="var(--orange)" d="M2 5h20v14H2z"/><path fill="none" stroke="var(--paper)" stroke-width="1.6" d="M2 5l10 8 10-8"/></svg>
        Derek@thecrateheron.com
      </p>
      <p class="address">4827 W. Ridge 918 S.<br>Harlow Springs, KS 72348</p>
    </div>

    <p class="website">www.<span class="website__domain">getcartonry</span>.com</p>
  </section>
</body>
</html>
```